Inner Courage: How to Feel Worthy, Step Through Fear and Empower Your Truth

Hello! I'm looking for a very professional-looking ebook cover (to be used for hardcopy as well). I'm looking for a design Similar to "Quiet Ember" by Dorian Petchey or Driftlines by Everett Sandholm (Examples included in attachments). I love how these nonfiction design covers have a white background, with attention-grabbing titles and clean, modern font that grabs the viewer's interest.
I've included sketches of my own that will be helpful to understand my vision for the design. I'm imagining the word "INNER" being thin, and either black or dark grey. I'm imagining the word "COURAGE" to be a deep red, like the underline in my logo (attached).
I'm not sure exactly if all-caps, or a mix of all-caps title and lowercase subtitle are best. I'll leave that to your professional opinion to feel out what gets the message through best and feels right.
In both of the book cover examples attached, there is great use of a sleek, clean image that exemplifies the message of the book. I am stuck here, not quite sure which image/item would be best there. Feel free to use your professional opinion there too!
Beneath all of the words, I would like the image of a tall, healthy green tree emerging from the clouds. I have been inspired by the view from an airplane window as you pop through the clouds, and would like to convey the same feeling of wonder while demonstrating that it's possible to stay grounding while growing to that level of wonder in your own life (hence the tree). I'd like there NOT to be an airplane wing or window edges in view though.
I am open to other ways to depict this sense of emerging into an experience of heaven on earth through presence and growth :)
Looking forward to what you come up with!

```html
<!DOCTYPE html>
<html lang="en">
<head>
<meta charset="UTF-8">
<title>Inner Courage — Book Cover</title>
<link rel="stylesheet" href="https://fonts.googleapis.com/css2?family=Cinzel:wght@400;700&display=swap">
<style>
  :root {
    --paper: #ffffff;
    --ink: #1e1e1e;
    --crimson: #b5141b;
    --leaf-light: #7aa04a;
    --leaf: #4f7d2c;
    --leaf-deep: #3d6622;
    --cloud-light: #efe7db;
    --cloud-warm: #d6c5ae;
    --cloud-mid: #9aa6b3;
    --cloud-shadow: #5a6c84;
  }
  html, body {
    margin: 0;
    padding: 0;
    overflow: hidden;
    background: var(--paper);
  }
  .cover {
    position: relative;
    width: 800px;
    height: 1200px;
    background: var(--paper);
    overflow: hidden;
    font-family: "Cinzel", "Times New Roman", serif;
  }
  .rule {
    position: absolute;
    left: 72px;
    width: 656px;
    height: 4px;
    background: var(--ink);
  }
  .rule--top { top: 106px; }
  .rule--bottom { top: 440px; }

  .title-line {
    position: absolute;
    left: 76px;
    width: 648px;
    display: flex;
    justify-content: space-between;
    margin: 0;
    line-height: 1;
  }
  .title-line span { display: block; }
  .title-inner {
    top: 150px;
    font-size: 114px;
    font-weight: 400;
    color: var(--ink);
  }
  .title-courage {
    top: 278px;
    left: 72px;
    width: 656px;
    font-size: 126px;
    font-weight: 400;
    color: var(--crimson);
  }

  .subtitle {
    position: absolute;
    top: 526px;
    left: 0;
    width: 800px;
    margin: 0;
    text-align: center;
    color: #000;
    font-size: 24px;
    font-weight: 700;
    letter-spacing: 0.5em;
    text-indent: 0.5em;
    line-height: 29.5px;
  }
  .subtitle .joiner {
    font-size: 17px;
    letter-spacing: 0.5em;
  }

  .hero-image {
    position: absolute;
    left: 0;
    top: 732px;
    width: 800px;
    height: 468px;
    background: linear-gradient(to bottom,
      var(--leaf-light) 0%,
      var(--leaf) 22%,
      var(--leaf-deep) 44%,
      var(--cloud-light) 56%,
      var(--cloud-warm) 72%,
      var(--cloud-mid) 88%,
      var(--cloud-shadow) 100%);
  }
</style>
</head>
<body>
  <main class="cover">
    <div class="rule rule--top"></div>
    <h1 class="title-line title-inner" aria-label="Inner">
      <span>I</span><span>N</span><span>N</span><span>E</span><span>R</span>
    </h1>
    <h1 class="title-line title-courage" aria-label="Courage">
      <span>C</span><span>O</span><span>U</span><span>R</span><span>A</span><span>G</span><span>E</span>
    </h1>
    <div class="rule rule--bottom"></div>

    <p class="subtitle">
      How to&nbsp; Understand Your Worth,<br>
      Step Through Fear<br>
      <span class="joiner">- and -</span><br>
      Emerge as a Leader
    </p>

    <div class="hero-image" role="img" aria-label="Photograph of a tall green leafy tree rising out of a sea of soft white clouds"></div>
  </main>
</body>
</html>
```